A Speech Therapy Business needs to update their logo

I need an update to the font and color of my logo to look more appealing. I am looking to open a private practice as a Speech Language Pathologist that caters to adults and children. It needs to be sophisticated and friendly at the same time. I want to keep the silhouette in my logo as is, just update the font and color for "Brightpaths".
Industry/Entity Type
Business
Contact Information for Business Card
I want the business card to have my logo, my name (Dorota Valk, CCC-SLP, TSSLD) and that I am a Bilingual Speech Language Pathologist. Also, include my phone number, (555) 271-8390. Include my website, Brightpathsslp.example, and email address, dorotavalk@brightpathsslp.example
Look and feel
Each slider illustrates characteristics of the customer's brand and the style your logo design should communicate.

```html
<!DOCTYPE html>
<html lang="en">
<head>
<meta charset="utf-8">
<title>Brightpaths – Business Card</title>
<link rel="stylesheet" href="https://fonts.googleapis.com/css2?family=Lato:wght@400;700&display=swap">
<style>
  :root {
    --page-bg: #e9e6e1;
    --card-bg: #ffffff;
    --brand-orange: #e8941f;
    --ink: #1c1c1c;
    --ink-soft: #2e2e2e;
    --band-black: #0d0d0d;
    --faint-figure: #f1f1f1;
  }
  * { box-sizing: border-box; margin: 0; padding: 0; }
  html, body {
    width: 1200px; height: 780px; overflow: hidden;
    background: var(--page-bg);
    font-family: "Lato", Arial, sans-serif;
  }
  .card {
    position: absolute; left: 100px; top: 100px;
    width: 1000px; height: 580px;
    background: var(--card-bg);
    border-radius: 22px;
    overflow: hidden;
    box-shadow: 0 10px 30px rgba(0,0,0,0.18);
  }
  .background-figures {
    position: absolute; left: 420px; top: 30px;
    width: 540px; height: 300px;
    border-radius: 40px;
    background: radial-gradient(ellipse at center, var(--faint-figure) 0%, rgba(241,241,241,0) 70%);
  }
  .brand {
    position: absolute; left: 64px; top: 150px;
    display: flex; align-items: center; gap: 14px;
  }
  .brand-dot {
    width: 26px; height: 26px; border-radius: 50%;
    background: var(--brand-orange);
  }
  .brand-name {
    font-weight: 700; font-size: 52px; line-height: 1;
    color: var(--brand-orange); text-transform: uppercase;
    letter-spacing: 0.5px;
  }
  .identity {
    position: absolute; right: 48px; top: 90px;
    width: 410px;
  }
  .identity-name {
    font-size: 25px; color: var(--brand-orange);
    text-transform: uppercase; letter-spacing: 0.3px; white-space: nowrap;
  }
  .identity-role {
    font-size: 20px; color: var(--ink); white-space: nowrap;
    padding-bottom: 8px; border-bottom: 1.5px solid var(--brand-orange);
    margin-top: 2px;
  }
  .website {
    position: absolute; right: 48px; top: 430px;
    font-size: 21px; color: var(--ink); letter-spacing: 0.3px;
  }
  .website .accent { color: var(--brand-orange); }
  .contact {
    position: absolute; left: 64px; top: 330px; width: 440px;
    border-top: 1.5px solid var(--brand-orange);
    padding-top: 60px;
  }
  .contact-row {
    display: flex; align-items: center; gap: 14px;
    font-size: 22px; color: var(--ink-soft); line-height: 1.45;
    white-space: nowrap;
  }
  .contact-icon {
    width: 26px; height: 26px; border-radius: 5px;
    background: var(--brand-orange);
    display: flex; align-items: center; justify-content: center;
    flex: none;
  }
  .band {
    position: absolute; left: 0; bottom: 0; height: 60px; width: 100%;
    display: flex;
  }
  .band-black { width: 58%; background: var(--band-black); }
  .band-orange { width: 42%; background: var(--brand-orange); }
</style>
</head>
<body>
  <section class="card">
    <div class="background-figures" role="img" aria-label="Faint silhouettes of walking children in the background"></div>

    <div class="brand">
      <span class="brand-dot"></span>
      <span class="brand-name">Brightpaths</span>
    </div>

    <div class="identity">
      <p class="identity-name">Dorota Valk, CCC-SLP, TSSLD</p>
      <p class="identity-role">Bilingual Speech Language Pathologist</p>
    </div>

    <p class="website">www.<span class="accent">Brightpathsslp</span>.example</p>

    <div class="contact">
      <p class="contact-row">
        <span class="contact-icon">
          <svg width="16" height="16" viewBox="0 0 24 24" aria-hidden="true">
            <path fill="#fff" d="M6.6 10.8a15.1 15.1 0 0 0 6.6 6.6l2.2-2.2a1 1 0 0 1 1-.25 11.4 11.4 0 0 0 3.6.57 1 1 0 0 1 1 1V20a1 1 0 0 1-1 1A17 17 0 0 1 3 4a1 1 0 0 1 1-1h3.5a1 1 0 0 1 1 1c0 1.250.2 2.45.57 3.6a1 1 0 0 1-.25 1z"/>
          </svg>
        </span>
        (555) 271-8390
      </p>
      <p class="contact-row">
        <span class="contact-icon">
          <svg width="16" height="16" viewBox="0 0 24 24" aria-hidden="true">
            <rect x="3" y="6" width="18" height="12" rx="1.5" fill="none" stroke="#fff" stroke-width="2"/>
            <path d="M3.5 7l8.5 6.5L20.5 7" fill="none" stroke="#fff" stroke-width="2"/>
          </svg>
        </span>
        dorotavalk@brightpathsslp.example
      </p>
    </div>

    <div class="band">
      <div class="band-black"></div>
      <div class="band-orange"></div>
    </div>
  </section>
</body>
</html>
```